Webdesign für Tischlerei Wendhaus
Merle Tannauer
Vielen Dank für das ansprechende, moderne und kundenbezogene Design
Zielgruppe
Tischlerei
Zielgruppe: Privat und Gewerbe wie Küchen, Praxen oder Schulen
Aufgabenstellung
Farben: braun/grün
keine Kopie der alten Seite
nutzerfreundliche Unternehmenswebseite
Logo und Slogan als jpeg-Datei vorhanden

```html
<!DOCTYPE html>
<html lang="de">
<head>
<meta charset="utf-8">
<title>Tischlerei Wendhaus</title>
<link href="https://fonts.googleapis.com/css2?family=Ubuntu:wght@400;500;700&display=swap" rel="stylesheet">
<style>
:root{
  --brown:#6a3322;
  --brown-dark:#5e2c1d;
  --text:#5a5a5a;
  --grey-icon:#c4c4c4;
  --field:#e1e1e1;
  --white:#ffffff;
}
*{margin:0;padding:0;box-sizing:border-box}
html,body{width:1200px;height:3528px;overflow:hidden;background:var(--white)}
body{position:relative;font-family:"Ubuntu",sans-serif;color:var(--text)}
.abs{position:absolute}
/* header */
.brand{left:90px;top:34px;font-size:30px;font-weight:700;color:var(--brown);line-height:1}
.phone{left:998px;top:31px;display:flex;align-items:center;gap:10px;font-size:14px;color:var(--brown-dark)}
.nav{top:86px;left:0;width:1200px;font-size:14px;color:var(--brown-dark)}
.nav a{position:absolute;color:inherit;text-decoration:none;white-space:nowrap}
/* photo bands */
.photo{left:0;width:1200px}
.hero{top:120px;height:449px;background:linear-gradient(120deg,#6b5748 0%,#8a7262 35%,#4f3f34 70%,#766457 100%)}
.hero-title{top:294px;left:0;width:1200px;text-align:center;font-size:44px;font-weight:700;color:var(--white)}
.hero-sub{top:352px;left:0;width:1200px;text-align:center;font-size:25px;font-weight:500;color:var(--white)}
.band-saw{top:1067px;height:214px;background:linear-gradient(100deg,#8a6a4c 0%,#b48a62 40%,#3b2c22 75%,#5a4533 100%)}
.band-design{top:2014px;height:214px;background:linear-gradient(100deg,#d8d2c8 0%,#e6e2dc 50%,#cfc8bd 100%)}
.band-logs{top:2662px;height:214px;background:linear-gradient(100deg,#5b4638 0%,#a07758 35%,#6c4a32 65%,#3b2f26 100%)}
/* sections */
.h2{font-size:30px;font-weight:500;color:var(--brown);line-height:40px}
.rule{width:75px;height:2px;background:var(--brown)}
.copy{font-size:13px;line-height:22.6px;color:var(--text)}
.btn{height:35px;width:162px;border:1.5px solid var(--brown);border-radius:18px;font-size:13px;font-weight:500;color:var(--brown-dark);display:flex;align-items:center;justify-content:center;background:var(--white)}
.placeholder{border-radius:4px}
.illu{left:692px;top:703px;width:377px;height:283px;background:radial-gradient(circle at 45% 45%,#c6c6c6 0%,#d8cfc9 45%,#fff 75%)}
.laptop{left:489px;top:2302px;width:607px;height:291px;background:linear-gradient(160deg,#e9e9ec 0%,#b9bcc2 60%,#f4f4f5 100%)}
/* services */
.svc-icon{width:80px;height:58px}
.svc-title{font-size:21px;font-weight:500;color:var(--brown);line-height:28.5px}
.arrows{left:973px;top:1940px;display:flex;gap:8px}
/* contact */
.h2-caps{font-size:30px;font-weight:500;color:var(--brown);line-height:40px;text-transform:uppercase}
.field{left:692px;width:420px;background:var(--field);font-size:13px;font-weight:500;color:#777;padding:16px 0 0 18px}
.check{left:692px;top:3269px;width:16px;height:16px;background:var(--brown)}
.consent{left:718px;top:3266px;width:395px;font-size:11px;line-height:16.5px;color:var(--text)}
.consent u{color:var(--brown-dark)}
/* footer */
.footer{left:0;top:3465px;width:1200px;height:63px;background:var(--brown);color:var(--white);font-size:11px}
.footer span{position:absolute;top:25px}
</style>
</head>
<body>

<header>
  <div class="abs brand">Tischlerei Wendhaus</div>
  <div class="abs phone">
    <svg width="18" height="18" viewBox="0 0 24 24" fill="none" stroke="#6a3322" stroke-width="1.6"><path d="M5 3h4l2 5-2.5 1.5a11 11 0 0 0 6 6L16 13l5 2v4a2 2 0 0 1-2 2A16 16 0 0 1 3 5a2 2 0 0 1 2-2z"/></svg>
    03722 418630
  </div>
  <nav class="abs nav">
    <a style="left:598px">Über uns</a>
    <a style="left:695px">Leistungen</a>
    <a style="left:808px">Service</a>
    <a style="left:900px">Planer</a>
    <a style="left:969px">Aktuelles</a>
    <a style="left:1063px">Kontakt</a>
  </nav>
</header>

<section>
  <div class="abs photo hero" role="img" aria-label="Foto: alter Holzhobel mit Hobelspänen auf einer Werkbank"></div>
  <h1 class="abs hero-title">Wir sind vom Fach!</h1>
  <p class="abs hero-sub">Der Holzweg? Das ist genau der richtige!</p>
</section>

<section>
  <h2 class="abs h2" style="left:174px;top:622px">Wer wir sind</h2>
  <div class="abs rule" style="left:174px;top:683px"></div>
  <div class="abs copy" style="left:174px;top:707px;width:440px">
    <p>Holz ist für mich ein wunderbarer Werkstoff. Die Maserungen, Farben, Düfte und Oberflächen dieses Materials sind ebenso vielfältig wie das, was man daraus "zaubern" kann.</p>
    <p style="margin-top:22.6px">Wer sich mit Holz umgibt, der lebt behaglich. Möbel, Wandverkleidungen, Türen und Fenster aus Holz geben uns jenes Stück Natur zurück, das im modernen Alltag häufig auf der Strecke bleibt.</p>
    <p style="margin-top:22.6px">Natürlich: Holz lebt - und braucht deshalb Pflege. Doch auch dabei unterstütze ich Sie gern und fachkundig.</p>
  </div>
  <div class="abs btn" style="left:174px;top:963px">Mehr erfahren</div>
  <div class="abs placeholder illu" role="img" aria-label="Illustration: Holzhammer und Stechbeitel auf einem Brett"></div>
</section>

<div class="abs photo band-saw" role="img" aria-label="Foto: Hände führen ein Brett an einer Kreissäge"></div>

<section>
  <h2 class="abs h2" style="left:174px;top:1333px;width:300px">Unsere Dienstleistungen</h2>
  <div class="abs rule" style="left:174px;top:1435px"></div>
  <p class="abs copy" style="left:174px;top:1460px;width:200px">Wir haben uns auf hochwertige Tischlerarbeiten spezialisiert.</p>
  <div class="abs btn" style="left:174px;top:1532px">Mehr erfahren</div>

  <!-- card 1 -->
  <svg class="abs svc-icon" style="left:519px;top:1349px" viewBox="0 0 80 58" fill="none" stroke="#6a3322" stroke-width="2">
    <circle cx="22" cy="32" r="21" fill="#c4c4c4" stroke="none"/>
    <rect x="26" y="6" width="26" height="48"/><line x1="39" y1="6" x2="39" y2="54"/>
    <rect x="52" y="28" width="27" height="24"/><line x1="52" y1="40" x2="79" y2="40"/>
    <line x1="62" y1="34" x2="68" y2="34"/><line x1="62" y1="46" x2="68" y2="46"/>
  </svg>
  <h3 class="abs svc-title" style="left:519px;top:1427px">Anfertigung von<br>Einbaumöbeln</h3>
  <p class="abs copy" style="left:519px;top:1504px;width:220px">Wir bieten Ihnen Möbel, gebaut ohne Schrauben und Nägel, ganz von Hand und aus Massivholz. Das ist die Königsklasse des Möbelbaus.</p>

  <!-- card 2 -->
  <svg class="abs svc-icon" style="left:815px;top:1344px" viewBox="0 0 80 63" fill="none" stroke="#6a3322" stroke-width="2">
    <circle cx="22" cy="37" r="21" fill="#c4c4c4" stroke="none"/>
    <path d="M22 60 V48 H32 V38 H42 V28 H52 V18 H62 V8 H72"/>
    <line x1="22" y1="44" x2="70" y2="6"/><line x1="30" y1="44" x2="30" y2="60"/>
    <line x1="74" y1="2" x2="74" y2="60"/><line x1="40" y1="36" x2="40" y2="60"/>
  </svg>
  <h3 class="abs svc-title" style="left:815px;top:1427px">Treppen und<br>Treppenrenovierung</h3>
  <p class="abs copy" style="left:815px;top:1504px;width:220px">Wir bieten Ihnen Möbel, gebaut ohne Schrauben und Nägel, ganz von Hand und aus Massivholz. Das ist die Königsklasse des Möbelbaus.</p>

  <!-- card 3 -->
  <svg class="abs svc-icon" style="left:519px;top:1644px" viewBox="0 0 80 58" fill="none" stroke="#6a3322" stroke-width="2">
    <circle cx="22" cy="32" r="21" fill="#c4c4c4" stroke="none"/>
    <path d="M28 14 L50 4 L72 12 L50 22 Z"/><path d="M28 24 L50 34 L72 22"/>
    <path d="M28 34 L50 44 L72 32"/><path d="M28 44 L50 54 L72 42"/>
    <line x1="28" y1="14" x2="28" y2="44"/><line x1="72" y1="12" x2="72" y2="42"/>
  </svg>
  <h3 class="abs svc-title" style="left:519px;top:1717px">Bauelemente aus<br>Kunststoff und Alu</h3>
  <p class="abs copy" style="left:519px;top:1794px;width:220px">Wir bieten Ihnen Möbel, gebaut ohne Schrauben und Nägel, ganz von Hand und aus Massivholz. Das ist die Königsklasse des Möbelbaus.</p>

  <!-- card 4 -->
  <svg class="abs svc-icon" style="left:815px;top:1644px" viewBox="0 0 80 58" fill="none" stroke="#6a3322" stroke-width="2">
    <circle cx="22" cy="32" r="21" fill="#c4c4c4" stroke="none"/>
    <rect x="28" y="2" width="46" height="54"/><rect x="33" y="7" width="17" height="44"/><rect x="52" y="7" width="17" height="44"/>
    <line x1="38" y1="14" x2="42" y2="24"/>
  </svg>
  <h3 class="abs svc-title" style="left:815px;top:1717px">Beschlags- und<br>Verglasungsarbeiten</h3>
  <p class="abs copy" style="left:815px;top:1794px;width:220px">Wir bieten Ihnen Möbel, gebaut ohne Schrauben und Nägel, ganz von Hand und aus Massivholz. Das ist die Königsklasse des Möbelbaus.</p>

  <div class="abs arrows">
    <svg width="22" height="22" viewBox="0 0 22 22" fill="none" stroke="#3a2a22" stroke-width="1.5"><circle cx="11" cy="11" r="10"/><path d="M13 6l-5 5 5 5"/></svg>
    <svg width="22" height="22" viewBox="0 0 22 22" fill="none" stroke="#3a2a22" stroke-width="1.5"><circle cx="11" cy="11" r="10"/><path d="M9 6l5 5-5 5"/></svg>
  </div>
</section>

<div class="abs photo band-design" role="img" aria-label="Foto: Hand mit Stift an Stuhlmodellen aus Holz auf Entwurfszeichnungen"></div>

<section>
  <h2 class="abs h2" style="left:174px;top:2323px;width:320px">Realisieren Sie Ihre Wunschmöbel</h2>
  <div class="abs rule" style="left:174px;top:2425px"></div>
  <p class="abs copy" style="left:174px;top:2451px">Möbelplaner</p>
  <div class="abs btn" style="left:174px;top:2495px">Zum Planer</div>
  <div class="abs placeholder laptop" role="img" aria-label="Laptop mit geöffnetem Möbelplaner und Raumbeispielen"></div>
</section>

<div class="abs photo band-logs" role="img" aria-label="Foto: gestapelte Baumstämme im Wald"></div>

<section>
  <h2 class="abs h2-caps" style="left:174px;top:2939px;width:480px">Fordern Sie ein kostenloses Angebot bei uns an:</h2>
  <div class="abs rule" style="left:174px;top:3040px"></div>
  <div class="abs copy" style="left:174px;top:3066px">
    <p>Lindenhofweg 14<br>09247 Ahornfelde</p>
    <p style="margin-top:22.6px">Fon 03722 418630<br>Fax 03722 418635<br>Mobil 0171 6628174</p>
    <p style="margin-top:22.6px">mail@tischlerei-wendhaus.de<br>www.tischlerei-wendhaus.de</p>
  </div>

  <div class="abs field" style="top:2951px;height:41px">Name</div>
  <div class="abs field" style="top:3003px;height:41px">Vorname</div>
  <div class="abs field" style="top:3055px;height:41px;padding-top:12px">E-Mailadresse</div>
  <div class="abs field" style="top:3107px;height:147px">Ihre Nachricht</div>
  <div class="abs check"></div>
  <p class="abs consent">Ich habe die <u>Datenschutzerklärung</u> zur Kenntnis genommen. Ich stimme zu, dass meine Angaben und Daten zur Beantwortung meiner Anfrage elektronisch erhoben und gespeichert werden. Hinweis: Sie können Ihre Einwilligung jederzeit für die Zukunft per E-Mail an <u>mail@tischlerei-wendhaus.de</u> widerrufen.</p>
  <div class="abs btn" style="left:692px;top:3363px">Senden</div>
</section>

<footer class="abs footer">
  <span style="left:94px">Datenschutz</span>
  <span style="left:189px">AGB</span>
  <span style="left:243px">Impressum</span>
  <span style="left:331px">Cookie-Einstellungen</span>
  <span style="right:88px">©2024 tischlerei-wendhaus</span>
</footer>

</body>
</html>
```